Business Card Design

We need a business card design for a new company located in Missouri City, TX, entitled 'Brightmere Chiropractic & Holistic Center'. Our services include restoration of health and vitality, spinal exam, health assessment, dietary & fitness programs, lymphatic & therapeutic massage, detox & remineralize body wraps, far infrared sauna therapy

Industry/Entity Type

Business

Contact Information for Business Card

Brightmere Chiropractic & Holistic Center, Marlena Voss LMT, 4125 Hwy. 9, Suite 300, Missouri City, TX 77312, 281-555-0193

```html
<!DOCTYPE html>
<html lang="en">
<head>
<meta charset="utf-8">
<title>Brightmere Chiropractic &amp; Holistic Center – Business Card</title>
<link rel="stylesheet" href="https://fonts.googleapis.com/css2?family=Open+Sans:ital,wght@0,400;0,600;1,400&display=swap">
<style>
  :root {
    --pink: #e36db5;
    --green: #bcd64e;
    --green-deep: #9dbf35;
    --paper: #fbfbfa;
    --ink: #2c2c2c;
    --stage: #e9e6df;
  }
  * { margin: 0; padding: 0; box-sizing: border-box; }
  html, body { width: 1200px; height: 780px; overflow: hidden; }
  body {
    background: var(--stage);
    font-family: "Open Sans", sans-serif;
    color: var(--ink);
  }
  .sheet {
    position: relative;
    width: 1200px;
    height: 780px;
    display: flex;
    align-items: center;
    justify-content: center;
    gap: 40px;
  }
  .card {
    position: relative;
    width: 540px;
    height: 310px;
    border-radius: 14px;
    overflow: hidden;
    background: var(--paper);
    box-shadow: 0 6px 18px rgba(0,0,0,.18);
  }
  .card-art { position: absolute; inset: 0; }

  /* front */
  .person { position: absolute; top: 22px; right: 30px; text-align: right; }
  .person-name { font-weight: 600; font-size: 25px; color: var(--pink); line-height: 1.1; }
  .person-title { font-size: 13px; margin-top: 2px; }
  .contacts { position: absolute; top: 86px; right: 30px; list-style: none; text-align: right; }
  .contact {
    display: flex; align-items: center; justify-content: flex-end;
    gap: 8px; font-size: 13px; line-height: 22px;
  }
  .contact-icon {
    width: 16px; height: 16px; border-radius: 3px; background: var(--pink);
    display: inline-flex; align-items: center; justify-content: center;
  }
  .brand {
    position: absolute; left: 28px; top: 132px;
    display: flex; align-items: center; gap: 14px;
  }
  .brand-dot {
    width: 58px; height: 58px; border-radius: 50%;
    background: radial-gradient(circle, #eef5cf 0%, #d7e99a 100%);
    flex: none;
  }
  .brand-name {
    font-weight: 400;
    font-size: 15px; line-height: 1.3; color: var(--pink); letter-spacing: .5px;
    text-transform: uppercase;
  }
  .address {
    position: absolute; right: 26px; bottom: 24px;
    text-align: right; font-size: 13.5px; line-height: 1.45; color: var(--ink);
    font-style: normal;
  }

  /* back */
  .services {
    position: absolute; left: 0; right: 0; top: 138px;
    text-align: center; list-style: none;
    font-size: 12.5px; line-height: 1.7; color: #3a3a3a; letter-spacing: .2px;
  }
</style>
</head>
<body>
<main class="sheet">

  <section class="card card-front" aria-label="Business card front">
    <svg class="card-art" viewBox="0 0 540 310" aria-hidden="true">
      <defs>
        <linearGradient id="frontGreen" x1="0" y1="1" x2="1" y2="0">
          <stop offset="0" stop-color="var(--green-deep)"/>
          <stop offset="1" stop-color="var(--green)"/>
        </linearGradient>
      </defs>
      <path d="M0,270 C210,262 400,214 540,168 L540,176 C400,226 230,286 0,298 Z" fill="var(--pink)"/>
      <path d="M0,310 L0,306 C240,294 410,236 540,186 L540,310 Z" fill="url(#frontGreen)"/>
    </svg>

    <header class="person">
      <h1 class="person-name">Marlena Voss LMT</h1>
      <p class="person-title">Managing Director</p>
    </header>

    <ul class="contacts">
      <li class="contact">281-555-0193
        <span class="contact-icon"><svg width="10" height="10" viewBox="0 0 24 24"><path fill="#fff" d="M6.6 10.8a15 15 0 0 0 6.6 6.6l2.2-2.2c.3-.3.7-.4 1-.2 1.1.4 2.3.6 3.6.6.6 0 1 .4 1 1V20c0 .6-.4 1-1 1A17 17 0 0 1 3 4c0-.6.4-1 1-1h3.5c.6 0 1 .4 1 1 0 1.2.2 2.4.6 3.6.1.3 0 .7-.2 1Z"/></svg></span>
      </li>
      <li class="contact">hello@brightmerehealth.com
        <span class="contact-icon"><svg width="10" height="10" viewBox="0 0 24 24"><path fill="#fff" d="M2 5h20v14H2Zm2 2v.5l8 5 8-5V7Z"/></svg></span>
      </li>
      <li class="contact">brightmerehealth.com
        <span class="contact-icon"><svg width="10" height="10" viewBox="0 0 24 24"><circle cx="12" cy="12" r="9" fill="none" stroke="#fff" stroke-width="2"/><path d="M3 12h18M12 3c3 3 3 15 0 18M12 3c-3 3-3 15 0 18" fill="none" stroke="#fff" stroke-width="1.6"/></svg></span>
      </li>
    </ul>

    <div class="brand">
      <span class="brand-dot" aria-hidden="true"></span>
      <p class="brand-name">Brightmere Chiropractic<br>&amp; Holistic Center</p>
    </div>

    <address class="address">4125 Hwy. 9, Suite 300,<br>Missouri City, TX 77312</address>
  </section>

  <section class="card card-back" aria-label="Business card back">
    <svg class="card-art" viewBox="0 0 540 310" aria-hidden="true">
      <defs>
        <linearGradient id="backGreen" x1="0" y1="0" x2="1" y2="1">
          <stop offset="0" stop-color="var(--green)"/>
          <stop offset="1" stop-color="var(--green-deep)"/>
        </linearGradient>
      </defs>
      <path d="M0,0 H540 V28 C360,34 150,58 0,108 Z" fill="url(#backGreen)"/>
      <path d="M0,124 C150,72 360,46 540,42 L540,47 C360,54 160,82 0,140 Z" fill="var(--pink)"/>
      <path d="M0,258 C180,256 380,232 540,172 L540,188 C380,248 180,268 0,268 Z" fill="var(--pink)"/>
      <path d="M0,282 C190,280 390,258 540,204 V310 H0 Z" fill="url(#backGreen)"/>
    </svg>

    <ul class="services">
      <li>restoration of health and vitality | spinal exam | health assessment</li>
      <li>dietary &amp; fitness programs | lymphatic &amp; therapeutic massage</li>
      <li>detox &amp; remineralize body wraps | far infrared sauna therapy</li>
    </ul>
  </section>

</main>
</body>
</html>
```